logo & Business Card Design

NovaGuard Termite & Pest Control, I need a great logo, take my ideas and run with them!
I will use this in marketing and website so needs to be eye catching but professional

Target Market(s)

Resedintial & Business

Industry/Entity Type

Marketing

Contact Information for Business Card

Need front side with pertinent info & Logo; back side will have a 25% off initial services Coupon!

Font styles to use
Sans Serif

Colors
ec1f27
1b1b1b

Requirements
Must have
• Professional logo and style
Nice to have
• Raised lettering, black, red, white colors maybe? I'm flexible, but those colors go good on any background, vehicle, uniform, etc...
Should not have
• Cheesy

```html
<!DOCTYPE html>
<html lang="en">
<head>
<meta charset="utf-8">
<title>NovaGuard Termite &amp; Pest Control – Business Card</title>
<link href="https://fonts.googleapis.com/css2?family=Lato:wght@400;700&display=swap" rel="stylesheet">
<style>
  :root {
    --backdrop: #3a3634;
    --card: #1d1e20;
    --card-edge: #141516;
    --text-light: #eef0f2;
    --text-muted: #c9ccd0;
    --accent-red: #d9421f;
    --divider: #3a3c3f;
    --mark: #8fa6c2;
  }
  * { margin: 0; padding: 0; box-sizing: border-box; }
  html, body {
    width: 1200px;
    height: 844px;
    overflow: hidden;
    background: var(--backdrop);
    font-family: "Lato", Arial, sans-serif;
  }
  .canvas {
    position: relative;
    width: 1200px;
    height: 844px;
  }
  .card {
    position: absolute;
    top: 278px;
    width: 504px;
    height: 288px;
    background: linear-gradient(160deg, #25272a 0%, var(--card) 55%, var(--card-edge) 100%);
    border-radius: 3px;
    box-shadow: 0 10px 28px rgba(0,0,0,0.45);
  }
  .card-front { left: 66px; }
  .card-back { left: 630px; }

  /* Brand lockup */
  .brand {
    display: flex;
    align-items: center;
    gap: 10px;
    color: var(--text-light);
    font-weight: 700;
    font-size: 26px;
    letter-spacing: 0.3px;
  }
  .brand-square {
    width: 16px;
    height: 16px;
    background: var(--mark);
  }
  .brand-sub {
    margin-top: 6px;
    color: var(--text-muted);
    font-size: 11px;
    letter-spacing: 1.6px;
    text-transform: uppercase;
  }

  /* Front */
  .front-brand {
    position: absolute;
    left: 34px;
    top: 112px;
  }
  .front-divider {
    position: absolute;
    left: 262px;
    top: 44px;
    width: 1px;
    height: 200px;
    background: var(--divider);
  }
  .contact {
    position: absolute;
    left: 290px;
    top: 62px;
    color: var(--text-light);
  }
  .contact-name {
    font-size: 24px;
    font-weight: 400;
    line-height: 1.1;
  }
  .contact-role {
    color: var(--accent-red);
    font-size: 14px;
    margin-top: 2px;
  }
  .contact-lines {
    list-style: none;
    margin-top: 20px;
    font-size: 13.5px;
    line-height: 1.35;
  }
  .contact-label { color: var(--accent-red); }
  .contact-address {
    margin-top: 18px;
    font-size: 13.5px;
    line-height: 1.35;
  }

  /* Back */
  .back-brand {
    position: absolute;
    left: 0;
    right: 0;
    top: 92px;
    display: flex;
    flex-direction: column;
    align-items: center;
  }
  .back-brand .brand { font-size: 34px; }
  .tagline {
    position: absolute;
    left: 0;
    right: 0;
    bottom: 44px;
    text-align: center;
    color: var(--text-muted);
    font-size: 13px;
  }
</style>
</head>
<body>
<main class="canvas">
  <section class="card card-front" aria-label="Business card front">
    <div class="front-brand">
      <div class="brand"><span class="brand-square"></span>NovaGuard</div>
      <div class="brand-sub">Termite &amp; Pest Control</div>
    </div>
    <div class="front-divider"></div>
    <div class="contact">
      <h1 class="contact-name">Daniel Reyes</h1>
      <p class="contact-role">Managing Director</p>
      <ul class="contact-lines">
        <li><span class="contact-label">T:</span> 044-555 218 904</li>
        <li><span class="contact-label">E:</span> info@novaguardpest.com</li>
        <li><span class="contact-label">W:</span> www.novaguardpest.com</li>
      </ul>
      <p class="contact-address">482, Harbor Line Road<br>Eastvale, 560218.</p>
    </div>
  </section>

  <section class="card card-back" aria-label="Business card back">
    <div class="back-brand">
      <div class="brand"><span class="brand-square"></span>NovaGuard</div>
      <div class="brand-sub">Termite &amp; Pest Control</div>
    </div>
    <p class="tagline">“A Shield of protection For Your Home”</p>
  </section>
</main>
</body>
</html>
```